Book Title: “Harbor: Road of Quiet Mercy” Please see the attachment “Text on the cover”.

Book Cover Design Instructions: This book is meant for people of all religions and nationalities. Therefore, on the cover, there should be no mosque or an object specific to any religion. The primary emphasis should be on the "unconditional love of God." Therefore, use universal symbols of love. The second priority themes could be Sufism, Peace, and self-improvement. Rest is your imagination. Please also see the attachment: 'Book description and author's Bio.'
This book has the potential to be a best seller. Please do a good job.
What Book Cover Formats are required: A designer should submit cover designs in three formats: (1) eBook, (2) Paperback, and (3) Hardback. These books will be published on Veltrano PBX.
Format requirements for eBooks are available from: https://pub.veltrano.example/en_US/help/topic/K481207735.
You can find paperback and hardback cover measurements from: https://pub.veltrano.example/en_US/cover-calculator
• To complete the project, all three formats should be accepted by Veltrano PBX.
• The book interior trim size is 6.14 X 9.21 inches.
• Interior Type: Premium color.
• No bleed.
• I do not upload barcode. So, the back cover should have room for Veltrano to print the barcode.
• Number of pages 126.
Compensation for the designer: After selecting one designer, I will increase the amount by $200 on Brushmarket to compensate for three deliverables.
Follow-up of the Project:
After the book is published, I may need minor revisions. For example, the number of pages may change. Therefore, I will need the same design in revised sizes. In that case, I will pay $25 for each revision. For example, if the number of pages changes, I will need a different spine for paperback and hardback, then I will pay the artist $25 + $25 = $50 for both designs.
List of Enclosers:
1. Text on the cover.
2. Book description and author's Bio for the back cover.
3. Later, I will upload my picture for the book's back cover.

Target Market(s)

Any adult

Industry/Entity Type

Any industry

Requirements
Must have
• Three Deliverables

```html
<!DOCTYPE html>
<html lang="en">
<head>
<meta charset="utf-8">
<title>Harbor: Road of Quiet Mercy — Book Cover</title>
<link href="https://fonts.googleapis.com/css2?family=Cinzel:wght@400;600;700&family=Montserrat:wght@400&display=swap" rel="stylesheet">
<style>
  :root {
    --stage: #000000;
    --paper: #ffffff;
    --gold: #9c7a33;
    --gold-dark: #8a6a2a;
    --gold-light: #f3e3a4;
    --ink: #1a1a1a;
    --gold-gradient: linear-gradient(180deg, #a8863d 0%, #c9a85a 35%, #f4e4a6 55%, #b8954a 75%, #8e6c2c 100%);
  }
  * { box-sizing: border-box; margin: 0; padding: 0; }
  html, body { width: 1200px; height: 1200px; overflow: hidden; background: var(--stage); }
  .canvas { position: relative; width: 1200px; height: 1200px; background: var(--stage); }
  .cover { position: absolute; left: 81px; top: 224px; width: 1037px; height: 752px; background: var(--paper); overflow: hidden; }
  .abs { position: absolute; }
  .caps { text-transform: uppercase; }

  /* Back cover */
  .back-title { left: 35px; top: 38px; width: 433px; font-family: "Cinzel", serif; font-weight: 700; font-size: 24px; line-height: 30px; letter-spacing: 1px; white-space: nowrap; color: var(--gold); text-align: justify; text-align-last: justify; }
  .back-subtitle { left: 35px; top: 78px; width: 433px; font-family: "Cinzel", serif; font-weight: 600; font-size: 12.6px; line-height: 18px; letter-spacing: .4px; white-space: nowrap; color: var(--gold); text-align: justify; text-align-last: justify; }
  .back-copy { left: 34px; top: 102px; width: 434px; font-family: "Montserrat", sans-serif; font-size: 10.5px; line-height: 12px; color: var(--ink); text-align: justify; }
  .back-copy p + p { margin-top: 12px; }
  .author-photo { left: 34px; top: 521px; width: 126px; height: 158px; border: 1px solid var(--gold); }
  .bio-name { left: 176px; top: 513px; font-family: "Cinzel", serif; font-weight: 600; font-size: 19px; line-height: 26px; letter-spacing: 1px; color: var(--gold); white-space: nowrap; }
  .bio-text { left: 175px; top: 547px; width: 293px; font-family: "Montserrat", sans-serif; font-size: 10.5px; line-height: 12px; color: var(--ink); text-align: justify; }
  .barcode-space { left: 290px; top: 622px; width: 180px; height: 97px; border: 1px solid var(--gold); }

  /* Spine */
  .spine-title, .spine-author { writing-mode: vertical-rl; font-family: "Cinzel", serif; font-weight: 600; font-size: 20px; letter-spacing: 1px; color: var(--gold); white-space: nowrap; left: 506px; }
  .spine-title { top: 44px; }
  .spine-author { top: 509px; }

  /* Front cover */
  .top-frame { left: 539px; top: 6px; width: 495px; height: 288px; }
  .front-author { left: 539px; top: 180px; width: 495px; text-align: center; font-family: "Cinzel", serif; font-weight: 600; font-size: 25px; line-height: 32px; letter-spacing: 1px; color: var(--gold); }
  .emblem { left: 611px; top: 278px; width: 78px; height: 78px; border-radius: 50%; background: radial-gradient(circle at 60% 40%, #ffffff 0%, #f3e7c4 45%, #d4b572 80%, #ffffff 100%); }
  .gold-text { background: var(--gold-gradient); -webkit-background-clip: text; background-clip: text; color: transparent; font-family: "Cinzel", serif; font-weight: 700; text-align: center; white-space: nowrap; left: 539px; width: 495px; }
  .title-main { top: 341px; font-size: 96px; line-height: 96px; letter-spacing: 1px; }
  .title-line2 { top: 430px; font-size: 68px; line-height: 76px; letter-spacing: 1px; }
  .title-line3 { top: 492px; font-size: 45px; line-height: 56px; letter-spacing: 2px; }
  .front-subtitle { left: 539px; top: 578px; width: 495px; text-align: center; font-family: "Cinzel", serif; font-weight: 600; font-style: italic; font-size: 24px; line-height: 30px; color: var(--gold); letter-spacing: .5px; }
  .base-band { left: 539px; top: 678px; width: 495px; height: 69px; border: 2px solid var(--gold); }
  .base-band-fill { position: absolute; left: 10px; top: 11px; right: 10px; bottom: 11px; border: 2px solid var(--gold); background: linear-gradient(90deg, #d8c28a, #efe2b8 50%, #d8c28a); }
</style>
</head>
<body>
<div class="canvas">
  <div class="cover">
    <!-- Back cover -->
    <h2 class="abs back-title caps">Harbor: Road of Quiet Mercy</h2>
    <h3 class="abs back-subtitle caps">Guide to Cultivating Inner Peace and Mindful Living</h3>
    <div class="abs back-copy">
      <p>This book intricately intertwines the diverse teachings of Sufism with the deep wisdom of the Quran to create a comprehensive roadmap for personal spiritual growth. The reader has a chance to experience firsthand the profound peace and boundless love Sufis have cherished for centuries. This book addresses the following critical questions:</p>
      <p>How can one unconditionally love God? It is the greatest of all kinds of love that ignites a profound and transformative spiritual journey.</p>
      <p>How to feel the love of God, which can bring immense peace and contentment.</p>
      <p>How to unconditionally love yourself, which nurtures personal growth and harmony.</p>
      <p>What is the most effective way to respond to life’s critical crises to reduce suffering and expedite recovery?</p>
      <p>This book also explores Islam’s overwhelming emphasis on avoiding Zulm (oppression and injustice) because the Quran mentions the word Zulm an astounding 291 times. Avoiding Zulm in all human interactions should be the top priority for every Muslim.</p>
      <p>The Prophet (PBUH) did not just preach peace and love. He gave us a practical example when he took over as a ruler of the Medina without bloodshed. He did not inherit power through the dynasty, and Medina was multi-religious. Arguably, it was history’s first large-scale peaceful transfer of power.</p>
      <p>Similarly, he signed the Treaty of Hudaybia with the staunchest enemy, employing an unprecedented peaceful strategy to nonviolently end a bitter war that had claimed hundreds of lives.</p>
      <p>The highlight of this book is that it points to the methodology to acquire a fully satisfied and contented soul (Nafs-e-Mutma’inna) in practical steps, which is the goal of every Sufi wayfarer.</p>
    </div>
    <div class="abs author-photo" role="img" aria-label="Space for author photograph"></div>
    <h4 class="abs bio-name caps">Dr. Maren Talvi</h4>
    <p class="abs bio-text">Dr. Talvi holds a Master’s in Physics and a Master’s in Computer Science and worked as a Software Engineer. He earned his Ph.D. in Islamic Studies. He was one of the founders of a mosque in Virginia.</p>
    <div class="abs barcode-space" aria-label="Reserved space for barcode"></div>

    <!-- Spine -->
    <div class="abs spine-title caps">Harbor: Road of Quiet Mercy</div>
    <div class="abs spine-author caps">Dr. Maren Talvi</div>

    <!-- Front cover -->
    <svg class="abs top-frame" viewBox="0 0 495 288" role="img" aria-label="Soft gold patterned frame around a plain panel">
      <defs>
        <linearGradient id="frameTone" x1="0" y1="0" x2="1" y2="0">
          <stop offset="0" stop-color="#e2cf9c"/>
          <stop offset="0.5" stop-color="#f4ead0"/>
          <stop offset="1" stop-color="#e2cf9c"/>
        </linearGradient>
      </defs>
      <path fill="url(#frameTone)" fill-rule="evenodd" stroke="#9c7a33" stroke-width="2"
        d="M1,1 H494 V287 H1 Z
           M57,287 V112 Q57,72 97,72 H398 Q438,72 438,112 V287 Z"/>
    </svg>
    <div class="abs front-author caps">Dr. Maren Talvi</div>
    <div class="abs emblem" role="img" aria-label="Soft gold emblem"></div>
    <h1>
      <span class="abs gold-text title-main">HARBOR</span>
      <span class="abs gold-text title-line2">ROAD OF</span>
      <span class="abs gold-text title-line3">QUIET MERCY</span>
    </h1>
    <p class="abs front-subtitle">Guide to Cultivating Inner<br>Peace and Mindful Living</p>
    <div class="abs base-band">
      <div class="base-band-fill" role="img" aria-label="Gold patterned band"></div>
    </div>
  </div>
</div>
</body>
</html>
```